Packaging card/Wrap design for Wavelink Karaoke Microphone

We are looking for a design for a karaoke microphone packaging. Attached is a sample of a different brand of ours, it should NOT resemble this design, but should merely be considered as a example. The brand identity is vintolu.com (see the logo in the attached files. The product in question has the name "Zolt."
The die-cut shows a different brand of ours and we are knocking it off with the Zolt. brand
The art area has 4 sides with the following dimensions:
6.6x 5 inches (2 areas)
6.6x 3 inches (2 areas)
Please be creative and use only images that are license free. Wavelink logo and content are in the attached example.

Please note, this is the sleeve design for the product itself.

Target Market(s)

Online shoppers

Industry/Entity Type

Electronics

Requirements
Must have
• images, specs and info according to the attached file. Modern bold font and make minimalistic . The name 'Zolt.' should appear in large
Nice to have
• We will consider the best design and incorporate it as a basis for a stationary brand image and will become house-style of this new identity
Should not have
• any of the images or logos from the die-cut in the attachment.

```html
<!DOCTYPE html>
<html lang="en">
<head>
<meta charset="utf-8">
<title>Zolt. Sleeve</title>
<link rel="stylesheet" href="https://fonts.googleapis.com/css2?family=Quicksand:wght@300;400;500&display=swap">
<style>
  :root {
    --page-bg: #ebebea;
    --card-bg: #050608;
    --gold: #b8974a;
    --gold-bright: #f3d27e;
    --grey-text: #9a9a9a;
  }
  * { margin: 0; padding: 0; box-sizing: border-box; }
  html, body {
    width: 1200px;
    height: 1200px;
    overflow: hidden;
    background: var(--page-bg);
  }
  .sleeve {
    position: absolute;
    left: 119px;
    top: 226px;
    width: 963px;
    height: 687px;
    background: var(--card-bg);
    font-family: "Quicksand", sans-serif;
  }
  .product-name {
    position: absolute;
    left: 86px;
    top: 34px;
    font-size: 150px;
    font-weight: 400;
    line-height: 1;
    letter-spacing: 2px;
    color: var(--gold);
  }
  .product-tagline {
    position: absolute;
    left: 91px;
    top: 191px;
    font-size: 18px;
    font-weight: 400;
    letter-spacing: 0.3px;
    color: var(--grey-text);
  }
  .feature-marks {
    position: absolute;
    right: 84px;
    top: 103px;
    display: flex;
    gap: 18px;
    align-items: center;
  }
  .feature-mark {
    display: flex;
    align-items: center;
    gap: 7px;
    font-size: 15px;
    font-weight: 500;
    color: var(--gold);
  }
  .feature-dot {
    width: 18px;
    height: 18px;
    border-radius: 50%;
    background: var(--gold);
  }
  .product-art {
    position: absolute;
    left: 0;
    top: 0;
    width: 963px;
    height: 687px;
  }
  .website {
    position: absolute;
    right: 88px;
    top: 596px;
    font-size: 16px;
    font-weight: 400;
    letter-spacing: 0.4px;
    color: var(--gold);
  }
</style>
</head>
<body>
  <main class="sleeve">
    <h1 class="product-name">Zolt.</h1>
    <p class="product-tagline">PORTABLE MICROPHONE &amp; SPEAKER</p>

    <div class="feature-marks">
      <span class="feature-mark"><span class="feature-dot"></span>Vidora</span>
      <span class="feature-mark"><span class="feature-dot"></span>Wavelink</span>
    </div>

    <svg class="product-art" viewBox="0 0 963 687" role="img" aria-label="Microphone silhouette filled with glowing golden sound-equalizer bars">
      <defs>
        <linearGradient id="equalizer-glow" x1="0" y1="0" x2="0" y2="1">
          <stop offset="0" stop-color="#f3d27e" stop-opacity="0"/>
          <stop offset="0.35" stop-color="#c9a04a" stop-opacity="0.35"/>
          <stop offset="0.7" stop-color="#e0b862" stop-opacity="0.8"/>
          <stop offset="1" stop-color="#f3d27e" stop-opacity="0.9"/>
        </linearGradient>
      </defs>
      <path fill="url(#equalizer-glow)"
        d="M93,334 L883,334 L883,520 Q883,530 873,530 L525,536 L525,600 Q525,606 519,606
           L303,606 Q297,606 297,600 L297,556 L250,554 L160,560 Q112,560 100,540 L93,520 Z"/>
    </svg>

    <p class="website">www.vintolu.com</p>
  </main>
</body>
</html>
```